Saving Lives with Dental Sleep Medicine

Looking for a brochure to market Dental Sleep Medicine educational courses . Whoever wins this bid will be hired to design the rest of our marketing campaign.
Design should be clean, simple with a modern feel. Not busy. Our courses utilize the most modern technology available.
Brochure content is attached, if you can't fit it all that is ok, we can tweak the content later. We are more focused on the look and feel of this design.
This brochure is marketing a 2 day course so there needs to be a spot for date, location, time & cost. As well as a notice of where to register VelmoraLearning.com, info@velmoralearning.com or call 1.800.###.#### and registration fees.
Also need a spot for Dr. Pelloquist's bio (attached). It's too long so just leave as much space as you can and we can amend the content.
Thank you so much. Looking forward to your designs. VelmEd Team :-)
Updates
Hello,
We are hoping for a minimalist design. Not busy. Clean and simple. We can reduce and minimize verbiage as needed. Just looking for layout and design.
Target Market(s)
Dentists
Requirements
Must have
- Clean lines, simple feel, minimalist and modern. Same font as logo. Black, white, gray.
Should not have
- Busy look and feel

```html
<!DOCTYPE html>
<html lang="en">
<head>
<meta charset="utf-8">
<title>Sleep &amp; Airway Management in a Dental Clinic – Course Brochure</title>
<link rel="stylesheet" href="https://fonts.googleapis.com/css2?family=Montserrat:wght@300;400;500;600;700;800&display=swap">
<style>
  :root {
    --backdrop: #b3b2b3;
    --paper: #ffffff;
    --ink: #141414;
    --panel-black: #0c0c0c;
    --panel-gray: #e4e4e5;
    --rule-gray: #9a9aa3;
    --accent-red: #e04f5f;
    --text-light: #f2f2f2;
    --text-muted: #555;
  }
  * { margin: 0; padding: 0; box-sizing: border-box; }
  html, body {
    width: 1200px; height: 920px; overflow: hidden;
    background: var(--backdrop);
    font-family: "Montserrat", sans-serif;
    color: var(--ink);
  }
  .spread {
    position: absolute; left: 140px; top: 130px;
    width: 920px; height: 660px;
    display: flex;
    background: var(--paper);
  }
  .page { position: relative; width: 460px; height: 660px; }
  .page--bio { border-right: 1px solid #e6e6e6; }

  /* Bio page */
  .bio-panel {
    position: absolute; left: 34px; top: 34px; right: 34px; bottom: 34px;
    background: var(--panel-black);
    padding: 14px;
  }
  .bio-photo {
    width: 100%; height: 250px;
    background: linear-gradient(160deg, #8b8b8b 0%, #cfcfcf 45%, #3a3a3a 100%);
  }
  .bio-name {
    position: absolute; right: 14px; top: 240px;
    width: 240px; height: 34px;
    background: var(--accent-red);
    color: var(--ink);
    font-weight: 400; font-size: 22px; letter-spacing: 0.5px;
    display: flex; align-items: center; justify-content: center;
  }
  .bio-text {
    margin-top: 36px; padding: 0 6px;
    color: var(--text-light);
    font-size: 9.2px; line-height: 1.5; font-weight: 300;
    text-align: justify;
  }
  .bio-text p + p { margin-top: 10px; }

  /* Cover page */
  .cover-panel {
    position: absolute; left: 30px; top: 34px; right: 30px; bottom: 70px;
    background: var(--panel-gray);
  }
  .top-rules { position: absolute; top: 14px; right: 0; display: flex; gap: 8px; }
  .top-rules span { display: block; height: 4px; width: 116px; }
  .rule-gray { background: var(--rule-gray); }
  .rule-red { background: var(--accent-red); }

  .brand {
    position: absolute; left: 20px; top: 300px;
    transform: rotate(-90deg); transform-origin: left top;
    display: flex; align-items: center; gap: 10px;
  }
  .brand-mark { width: 16px; height: 16px; background: var(--accent-red); }
  .brand-name {
    font-weight: 300; font-size: 24px; color: var(--text-muted); letter-spacing: 0.3px;
  }

  .course { position: absolute; left: 150px; top: 70px; right: 20px; }
  .course-title { font-weight: 700; font-size: 14.5px; line-height: 1.2; }
  .course-sub { margin-top: 6px; font-size: 9.5px; font-weight: 400; line-height: 1.35; }

  .details { position: absolute; left: 78px; top: 190px; right: 20px; }
  .detail-date {
    font-size: 42px; font-weight: 400; letter-spacing: 1px;
    border-bottom: 2px solid var(--ink); padding-bottom: 2px; text-align: right;
  }
  .detail-time {
    font-size: 34px; font-weight: 800; text-align: right;
    border-bottom: 2px solid var(--ink); padding: 2px 0;
  }
  .detail-row { display: flex; align-items: center; gap: 12px; margin-top: 6px; }
  .detail-price { font-size: 40px; font-weight: 500; padding-right: 12px; border-right: 2px solid var(--ink); line-height: 1; }
  .detail-venue { font-size: 10.5px; font-weight: 500; line-height: 1.35; }

  .register {
    position: absolute; left: 0; right: 0; bottom: 0; height: 58px;
    background: var(--panel-black); color: var(--text-light);
    padding: 10px 16px;
  }
  .register-title { font-size: 12px; font-weight: 600; }
  .register-contact { margin-top: 5px; font-size: 9.5px; font-weight: 300; }
  .register-contact .sep { margin: 0 6px; }

  .bottom-rule {
    position: absolute; left: 30px; bottom: 58px;
    width: 200px; height: 4px; background: var(--accent-red);
  }
  .fees {
    position: absolute; right: 30px; bottom: 30px;
    width: 240px; height: 22px;
    background: var(--panel-black); color: var(--text-light);
    font-size: 10px; font-weight: 600;
    display: flex; align-items: center; justify-content: flex-end; padding-right: 10px;
  }
</style>
</head>
<body>
  <main class="spread">
    <section class="page page--bio">
      <div class="bio-panel">
        <div class="bio-photo" role="img" aria-label="Portrait photograph of Dr. Pelloquist in his office"></div>
        <h2 class="bio-name">Dr. Pelloquist's</h2>
        <div class="bio-text">
          <p>Dr. Pelloquist received his Doctor of Dental Surgery degree and Bachelor of Medical Sciences from a leading university. He also earned fellowships in dental sleep medicine and completed advanced training in airway care and oral appliance therapy at a renowned research hospital.</p>
          <p>Dr. Pelloquist is a general dentist who maintains a group of private practices with an interest in dental sleep medicine and TMD management. He is actively involved in clinical research and has lectured at many national and international meetings on digital workflows and oral appliance therapy for obstructive sleep apnea.</p>
          <p>He is the founder of a dental sleep medicine study club and serves as clinical director of a sleep centre. He is a strong advocate for collaboration between physicians, sleep dentists and other healthcare professionals, and has trained hundreds of dentists in dental sleep medicine.</p>
        </div>
      </div>
    </section>

    <section class="page page--cover">
      <div class="cover-panel">
        <div class="top-rules"><span class="rule-gray"></span><span class="rule-red"></span></div>

        <div class="brand">
          <span class="brand-mark"></span>
          <span class="brand-name">VelmoraLearning</span>
        </div>

        <div class="course">
          <h1 class="course-title">Sleep &amp; Airway<br>Management in a Dental Clinic</h1>
          <p class="course-sub">SomnaTrack Plus System &amp; Fully Digital Workflows<br>for OAT</p>
        </div>

        <div class="details">
          <div class="detail-date">01/01/2020</div>
          <div class="detail-time">09:30AM</div>
          <div class="detail-row">
            <span class="detail-price">$150</span>
            <span class="detail-venue">Address Goes Here<br>City Name, Zip Code</span>
          </div>
        </div>

        <div class="register">
          <div class="register-title">Where To Register</div>
          <div class="register-contact">VelmoraLearning.com<span class="sep">|</span>info@velmoralearning.com<span class="sep">|</span>call 1.800.###.####</div>
        </div>
      </div>
      <div class="bottom-rule"></div>
      <div class="fees">Registration Fees $100</div>
    </section>
  </main>
</body>
</html>
```